Portal Panel Medic need professional looking business card printed on plastic, Commericial, Industri

We are family owned and operated garage door company in Indianapolis, Indiana. We sale service and install dock equipment, doors, operators. We are looking to expand our commercial/ industrial division. We also service all residential doors and operators. We are looking for a business that stands out of the crowd. We are committed to have the best customer service in the industry.

Target Market(s)

National and local general contractors, National/ Corpate service accounts,

Industry/Entity Type

Business Service

Contact Information for Business Card

To be printed on plastic stock

Font styles to use
Sans Serif

Colors
ffffff
f04a50
ec1f27

Requirements
Must have
• Name, website,email, phone number, position.
Nice to have
• A standout professional design

```html
<!DOCTYPE html>
<html lang="en">
<head>
<meta charset="utf-8">
<title>Portal Panel Medic – Business Card</title>
<link rel="stylesheet" href="https://fonts.googleapis.com/css2?family=Open+Sans:wght@400;600&display=swap">
<style>
  :root {
    --red: #ec1f27;
    --coral: #f04a50;
    --salmon: #f4826a;
    --white: #ffffff;
    --backdrop: #d9d9d9;
  }
  * { box-sizing: border-box; margin: 0; padding: 0; }
  html, body {
    width: 1200px; height: 1000px; overflow: hidden;
    background: var(--backdrop);
    font-family: "Open Sans", Arial, sans-serif;
  }
  .card {
    position: absolute;
    width: 620px; height: 354px;
    overflow: hidden;
    box-shadow: 0 4px 10px rgba(0,0,0,0.18);
  }

  /* Front side */
  .card-front { left: 140px; top: 90px; background: var(--white); }
  .front-band {
    position: absolute; left: 0; top: 0; width: 100%; height: 166px;
    background: var(--red);
  }
  .position-tab {
    position: absolute; left: 170px; top: 148px; width: 420px; height: 44px;
    background: var(--salmon);
    border-radius: 0 0 24px 24px;
  }
  .person-name {
    position: absolute; left: 170px; top: 104px; width: 420px;
    text-align: center; color: var(--white);
    font-size: 28px; font-weight: 400; letter-spacing: 2px; line-height: 1.2;
  }
  .person-position {
    position: absolute; left: 170px; top: 148px; width: 420px;
    text-align: center; color: var(--white);
    font-size: 11px; letter-spacing: 1.5px; line-height: 18px;
  }
  .contact-list {
    position: absolute; left: 300px; top: 212px; list-style: none;
  }
  .contact-item {
    display: flex; align-items: center; gap: 16px;
    color: var(--red); font-size: 20px; letter-spacing: 1.5px;
    line-height: 28px; margin-bottom: 10px;
  }
  .contact-icon { width: 18px; height: 18px; flex: none; }

  /* Back side */
  .card-back { left: 440px; top: 520px; background: var(--red); }
  .back-frame {
    position: absolute; inset: 30px;
    border: 2px solid var(--white);
  }
  .brand-name {
    position: absolute; left: 0; top: 50%; width: 100%;
    transform: translateY(-50%);
    text-align: center;
    color: var(--white); font-weight: 600;
    font-size: 30px; line-height: 1.2; letter-spacing: 1px;
  }
</style>
</head>
<body>

<section class="card card-front" aria-label="Business card front">
  <div class="front-band"></div>
  <div class="position-tab"></div>
  <p class="person-name">NAME OF PERSON</p>
  <p class="person-position">POSITION</p>
  <ul class="contact-list">
    <li class="contact-item">
      <svg class="contact-icon" viewBox="0 0 24 24" aria-hidden="true"><path fill="#ec1f27" d="M6.6 10.8a15 15 0 0 0 6.6 6.6l2.2-2.2c.3-.3.7-.4 1-.2 1.1.4 2.3.6 3.6.6.6 0 1 .4 1 1V20c0 .6-.4 1-1 1A17 17 0 0 1 3 4c0-.6.4-1 1-1h3.5c.6 0 1 .4 1 1 0 1.3.2 2.5.6 3.6.1.3 0 .7-.2 1z"/></svg>
      <span>PHONE NUMBER</span>
    </li>
    <li class="contact-item">
      <svg class="contact-icon" viewBox="0 0 24 24" aria-hidden="true" fill="none" stroke="#ec1f27" stroke-width="2.2"><circle cx="12" cy="12" r="9.5"/><ellipse cx="12" cy="12" rx="4" ry="9.5"/><line x1="2.5" y1="12" x2="21.5" y2="12"/><path d="M4.5 7h15M4.5 17h15"/></svg>
      <span>WEBSITE</span>
    </li>
    <li class="contact-item">
      <svg class="contact-icon" viewBox="0 0 24 24" aria-hidden="true"><rect x="2" y="5" width="20" height="14" fill="#ec1f27"/><path d="M2.5 5.5 12 13l9.5-7.5" fill="none" stroke="#fff" stroke-width="1.6"/></svg>
      <span>EMAIL ADDRESS</span>
    </li>
  </ul>
</section>

<section class="card card-back" aria-label="Business card back">
  <div class="back-frame"></div>
  <p class="brand-name">Portal Panel Medic</p>
</section>

</body>
</html>
```